Mobile Money & Fintech Solutions needs a business card design and logo

I need the design of a business card and a logo for my consultant, based in Asuncion Paraguay. I am in the Digital World category, specializing in Mobile Money, Fintech Solutions & e-commerce. I would like the design to reflect trust and above all encompass the area of ​​specialty of the services that I offer. (Mobile Money, Fintech Solutions & e-commerce)

Target Market(s)

Financial entities, companies wishing to undertake a Fintech or e-commerce project

Contact Information for Business Card

Marela Quintobri
Senior Advisory Consultant
Cel +595983417258
Skype ID marelaquintobri
Linkedin: http://lnkshort.example/8wXpq4Tz

Logo Text

Fintech Solutions&E-commerce

Requirements
Must have
• I would like it to be a fusion of symbols, example of the @, the $, cellular (cell) that can encompass the areas.
Nice to have
• Must be related to the Fintech area and / or Mobile MOney and e-commerce. It is a new consultancy, so there are no previous logos

```html
<!DOCTYPE html>
<html lang="en">
<head>
<meta charset="UTF-8">
<title>NexoPago Business Card</title>
<link href="https://fonts.googleapis.com/css2?family=Lato:wght@400;700&display=swap" rel="stylesheet">
<style>
  :root {
    --backdrop: #2a2a2b;
    --card-dark: #1d1d1e;
    --card-light: #3b3b3c;
    --accent: #f26a12;
    --ink: #ffffff;
  }
  * { margin: 0; padding: 0; box-sizing: border-box; }
  html, body { width: 1200px; height: 900px; overflow: hidden; }
  body {
    background: var(--backdrop);
    font-family: "Lato", sans-serif;
    color: var(--ink);
    display: flex;
    flex-direction: column;
    align-items: center;
    justify-content: center;
    gap: 40px;
  }
  .card {
    width: 665px;
    height: 380px;
    background: radial-gradient(ellipse at 30% 45%, var(--card-light) 0%, var(--card-dark) 70%);
    position: relative;
  }
  .brand {
    display: flex;
    align-items: center;
    gap: 14px;
  }
  .brand-mark {
    width: 30px;
    height: 30px;
    background: var(--accent);
  }
  .brand-name {
    font-weight: 700;
    color: var(--ink);
    letter-spacing: 0.5px;
  }
  /* Front */
  .card-front {
    display: flex;
    flex-direction: column;
    align-items: center;
    justify-content: center;
    gap: 46px;
  }
  .card-front .brand-name { font-size: 56px; }
  .card-front .brand-mark { width: 40px; height: 40px; }
  .tagline {
    font-size: 17px;
    letter-spacing: 1px;
    display: flex;
    align-items: center;
    gap: 10px;
  }
  .tagline .dot {
    width: 7px; height: 7px; border-radius: 50%;
    background: var(--accent);
  }
  /* Back */
  .card-back {
    display: flex;
    align-items: center;
  }
  .card-back .brand {
    width: 330px;
    justify-content: center;
  }
  .card-back .brand-name { font-size: 38px; }
  .divider {
    width: 2px;
    height: 250px;
    background: var(--accent);
  }
  .contact {
    padding-left: 52px;
  }
  .person-name {
    color: var(--accent);
    font-weight: 700;
    font-size: 28px;
    line-height: 1.1;
  }
  .person-role {
    font-size: 19px;
    margin-bottom: 16px;
  }
  .address {
    font-size: 19px;
    line-height: 1.3;
    margin-bottom: 12px;
  }
  .contact-list { list-style: none; }
  .contact-list li {
    display: flex;
    align-items: center;
    gap: 14px;
    font-size: 19px;
    line-height: 1.5;
  }
  .contact-list svg {
    width: 18px; height: 18px;
    fill: var(--accent);
    flex: none;
  }
</style>
</head>
<body>
  <section class="card card-front">
    <div class="brand">
      <span class="brand-mark"></span>
      <span class="brand-name">NexoPago</span>
    </div>
    <p class="tagline">MOBILE MONEY <span class="dot"></span> FINTECH SOLUTIONS <span class="dot"></span> E-COMMERCE</p>
  </section>

  <section class="card card-back">
    <div class="brand">
      <span class="brand-mark"></span>
      <span class="brand-name">NexoPago</span>
    </div>
    <div class="divider"></div>
    <div class="contact">
      <p class="person-name">Tomas Riveral</p>
      <p class="person-role">Manager</p>
      <p class="address">1450 Calle Lomas<br>Vireo TX 78010</p>
      <ul class="contact-list">
        <li>
          <svg viewBox="0 0 24 24" aria-hidden="true"><path d="M6.6 10.8a15 15 0 0 0 6.6 6.6l2.2-2.2c.3-.3.7-.4 1-.2 1.1.4 2.3.6 3.6.6.6 0 1 .4 1 1V20c0 .6-.4 1-1 1A17 17 0 0 1 3 4c0-.6.4-1 1-1h3.5c.6 0 1 .4 1 1 0 1.3.2 2.5.6 3.6.1.3 0 .7-.2 1z"/></svg>
          555 014 2200
        </li>
        <li>
          <svg viewBox="0 0 24 24" aria-hidden="true"><path d="M6 2h12v5H6zM4 8h16a2 2 0 0 1 2 2v6h-4v-3H6v3H2v-6a2 2 0 0 1 2-2zm3 6h10v8H7z"/></svg>
          555 014 2201
        </li>
        <li>
          <svg viewBox="0 0 24 24" aria-hidden="true"><path d="M2 5h20v14H2zm2 2v.5l8 5 8-5V7l-8 5z"/></svg>
          info@nexopago.example
        </li>
        <li>
          <svg viewBox="0 0 24 24" aria-hidden="true"><path d="M12 2a10 10 0 1 0 0 20 10 10 0 0 0 0-20zm6.9 6h-3a15 15 0 0 0-1.3-3.9A8 8 0 0 1 18.9 8zM12 4c.8 1.2 1.5 2.5 1.9 4h-3.8c.4-1.5 1.1-2.8 1.9-4zM4.3 14a8 8 0 0 1 0-4h3.4a16 16 0 0 0 0 4zm.8 2h3a15 15 0 0 0 1.3 3.9A8 8 0 0 1 5.1 16zm3-8h-3a8 8 0 0 1 4.3-3.9C8.8 5.3 8.4 6.6 8.1 8zM12 20c-.8-1.2-1.5-2.5-1.9-4h3.8c-.4 1.5-1.1 2.8-1.9 4zm2.3-6H9.7a14 14 0 0 1 0-4h4.6a14 14 0 0 1 0 4zm.3 5.9c.6-1.2 1-2.5 1.3-3.9h3a8 8 0 0 1-4.3 3.9zm1.7-5.9a16 16 0 0 0 0-4h3.4a8 8 0 0 1 0 4z"/></svg>
          www.nexopago.example
        </li>
      </ul>
    </div>
  </section>
</body>
</html>
```